Consulting firm needs elegant, modern designs

Business card design - I have a logo which has previously been developed for Q-Pathways - I will attach. I will also attach specifications for the size of the business card.

We also need a logo design for our leadership consulting product - Form in Guidance - we focus on improving workplace health by educating leaders and learning professionals about how the physical and emotional affects performance and engagement. I have some example logos and ideas which I will attach - these have attempted to bring in the body but I do not like the font (see www.formingguidance-example.com for preferred font). Idea is to please have a 'body' visible somehow in the word Leadership, ensuring that this conveys flexibility and agility. Colors which I prefer are deep purple OR turquoise, together with silver. COLORS below are for LOGO design.

Target Market(s)

For the business card, it should be more masculine. The logo which will be attached should be neutralized into dark blue shades and silver. The business card Q-Pathways is focused on business transformation - organizations who would require a consultant to help them enter new markets, for example.

Industry/Entity Type

Leadership

Contact Information for Business Card

Content:
Q-Pathways
Lindenkade 27
4921KP, Breda, The Netherlands
maurits@Q-Pathways.example
www.Q-Pathways.example

Colors for business card should be conservative and slightly more masculine. Use the Q-Pathways logo but change the colors to blue or shades of gray/black.

Dimensions for cut
85 x 55 mm
1004 x 650 pixels
Full document size
88 x 58 mm
1040 x 685 pixels
For the best result, you need to design the full document size including the bleed

Logo Text

Form in Guidance

Font styles to use
Serif
Sans Serif

Colors
876aae
333333
959595

Requirements
Must have
• Professional, modern and unique business card design
• Professional, elegant, and modern logo design - with creative thinking
Should not have
• Too many colors

```html
<!DOCTYPE html>
<html lang="en">
<head>
<meta charset="utf-8">
<title>Q-Pathways business card</title>
<link rel="stylesheet" href="https://fonts.googleapis.com/css2?family=Montserrat:wght@600;700&family=Work+Sans:wght@400;500;600&display=swap">
<style>
  :root {
    --stage: #1f1f21;
    --night: #2b2652;
    --night-deep: #231f45;
    --ink: #262244;
    --violet: #4b3f94;
    --royal: #2f5d9c;
    --teal: #74c3bb;
    --grey: #5f5f66;
    --soft-grey: #8a8a92;
    --paper: #ffffff;
  }
  * { box-sizing: border-box; margin: 0; padding: 0; }
  html, body {
    width: 1200px; height: 852px; overflow: hidden;
    background: var(--stage);
    font-family: "Work Sans", Arial, sans-serif;
  }
  .stage { position: relative; width: 1200px; height: 852px; }
  .card {
    position: absolute; top: 251px;
    width: 540px; height: 350px;
    overflow: hidden;
    border-radius: 3px;
  }
  /* front side */
  .card--front {
    left: 40px;
    background: linear-gradient(135deg, var(--night-deep), var(--night) 60%, #332c5e);
  }
  .card--front .halo {
    position: absolute; left: 150px; top: 20px;
    width: 300px; height: 300px; border-radius: 50%;
    background: rgba(255,255,255,0.04);
  }
  .brand { position: absolute; display: flex; align-items: center; gap: 14px; }
  .brand__dot { width: 46px; height: 46px; border-radius: 50%; flex: none; }
  .brand__text { display: flex; flex-direction: column; }
  .brand__name {
    font-family: "Work Sans", Arial, sans-serif;
    font-weight: 600; font-size: 44px; line-height: 1; letter-spacing: 0.5px;
  }
  .brand__tagline {
    font-family: "Work Sans", Arial, sans-serif;
    font-weight: 400; font-size: 13px; letter-spacing: 1px; margin-top: 6px;
  }
  .card--front .brand { left: 96px; top: 140px; }
  .card--front .brand__dot { background: var(--teal); }
  .card--front .brand__name { color: var(--paper); }
  .card--front .brand__tagline { color: #d6d3e6; }

  /* back side */
  .card--back { left: 620px; background: var(--paper); }
  .card--back .brand { left: 298px; top: 86px; gap: 10px; }
  .card--back .brand__dot { width: 32px; height: 32px; background: var(--royal); }
  .card--back .brand__name { color: var(--ink); font-size: 28px; }
  .card--back .brand__tagline { color: var(--soft-grey); font-size: 10px; margin-top: 4px; }

  .holder { position: absolute; left: 0; top: 60px; }
  .holder__mark {
    position: absolute; left: 0; top: 2px;
    width: 7px; height: 28px; background: var(--violet);
  }
  .holder__name {
    margin-left: 36px;
    font-family: "Montserrat", Arial, sans-serif; font-weight: 700;
    font-size: 22px; letter-spacing: 3px; color: var(--violet);
  }
  .holder__role {
    margin-left: 30px; margin-top: 0;
    font-family: "Montserrat", Arial, sans-serif; font-weight: 700;
    font-size: 13px; letter-spacing: 1.5px; color: #333333;
  }
  .contacts { position: absolute; left: 26px; top: 140px; list-style: none; }
  .contacts li {
    display: flex; align-items: center; gap: 10px;
    font-size: 16px; color: var(--ink); line-height: 24px;
  }
  .contacts svg { width: 16px; height: 16px; flex: none; }
  .address { position: absolute; left: 22px; top: 205px; font-style: normal; }
  .address__company { font-size: 15px; font-weight: 500; color: var(--royal); margin-bottom: 4px; }
  .address__line { font-size: 15px; color: var(--grey); line-height: 21px; }
  .band { position: absolute; left: 0; bottom: 0; width: 100%; height: 14px; display: flex; }
  .band__left { width: 52%; background: var(--royal); }
  .band__right { flex: 1; background: var(--teal); }
</style>
</head>
<body>
<main class="stage">
  <section class="card card--front" aria-label="Card front">
    <div class="halo"></div>
    <div class="brand">
      <span class="brand__dot"></span>
      <div class="brand__text">
        <span class="brand__name">Q-Pathways</span>
        <span class="brand__tagline">Steady steps forward</span>
      </div>
    </div>
  </section>

  <section class="card card--back" aria-label="Card back">
    <div class="holder">
      <span class="holder__mark"></span>
      <p class="holder__name">DORIAN VELD</p>
      <p class="holder__role">CEO</p>
    </div>

    <ul class="contacts">
      <li>
        <svg viewBox="0 0 16 16" fill="none" stroke="#4b3f94" stroke-width="1.4"><rect x="1.5" y="3.5" width="13" height="9" rx="1"/><path d="M1.5 4l6.5 5 6.5-5"/></svg>
        maurits@Q-Pathways.example
      </li>
      <li>
        <svg viewBox="0 0 16 16" fill="none" stroke="#4b3f94" stroke-width="1.2"><circle cx="8" cy="8" r="6.5"/><ellipse cx="8" cy="8" rx="3" ry="6.5"/><path d="M1.5 8h13M2.5 5h11M2.5 11h11"/></svg>
        www.Q-Pathways.example
      </li>
    </ul>

    <address class="address">
      <p class="address__company">Q-Pathways</p>
      <p class="address__line">Lindenkade 27</p>
      <p class="address__line">4921KP, Breda, The Netherlands</p>
    </address>

    <div class="brand">
      <span class="brand__dot"></span>
      <div class="brand__text">
        <span class="brand__name">Q-Pathways</span>
        <span class="brand__tagline">Steady steps forward</span>
      </div>
    </div>

    <div class="band"><span class="band__left"></span><span class="band__right"></span></div>
  </section>
</main>
</body>
</html>
```